Bref créative
Calvane Chiropractic Stationary/Brochure/Business Card / Post-It Note Design
Calvane Chiropractic Motion and Vitality
Bright & Fun-filled
Marla Teversham, D.C., Diplomate Continental Spinal Council of Athletic Clinicians (w/ "registered' )
417 E Quarry Ln, Suite 83
PO Box 6289
Harrowby PA 18944-0562
Dr.Marla@GoDrMarla.net
www.GoDrMarla.net
* clarification- title should have registered symbol on it
*I would like a Post It Note Design that has
Business Name, Tag Line, Phone Number and " A table is reserved for you and a line to write in appointment time.
* Please include tag line
*I've uploaded both a black background & white background version. I prefer the black background for its pop of color but realized that modifications for letterhead & brochures may be necessary.
the back of the card should have:
Certified Practitioner in the Following:
and then upload logos for
QEL
Pulsetap Systems
KQP / TBVX
VHP
GQLBR
Steelstride Provider

```html
<!DOCTYPE html>
<html lang="en">
<head>
<meta charset="utf-8">
<title>Calvane Chiropractic Stationery</title>
<link rel="stylesheet" href="https://fonts.googleapis.com/css2?family=Cinzel:wght@400;700&family=Open+Sans:wght@400;600;700&display=swap">
<style>
  :root {
    --backdrop: #2e2e2e;
    --paper: #ffffff;
    --green: #8cc43c;
    --green-deep: #5f9a1c;
    --lime: #c2dc3a;
    --purple: #7a3d96;
    --purple-soft: #b597c8;
    --ink: #444;
    --card-black: #111;
  }
  * { box-sizing: border-box; margin: 0; padding: 0; }
  html, body { width: 1200px; height: 794px; overflow: hidden; }
  body { background: var(--backdrop); font-family: "Open Sans", sans-serif; position: relative; }

  .sheet { position: absolute; background: var(--paper); overflow: hidden; box-shadow: 0 4px 14px rgba(0,0,0,.45); }

  .brand { text-align: center; }
  .brand-mark { border-radius: 50%; background: var(--lime); display: inline-block; }
  .brand-name { font-family: "Cinzel", serif; font-weight: 700; color: var(--green-deep); line-height: 1; white-space: nowrap; }
  .brand-sub { font-family: "Cinzel", serif; font-weight: 700; color: var(--purple); line-height: 1.1; white-space: nowrap; }
  .brand-tag { font-family: "Cinzel", serif; font-weight: 700; color: var(--purple); line-height: 1.3; white-space: nowrap; }

  /* Letterhead */
  .letterhead { left: 36px; top: 38px; width: 521px; height: 730px; }
  .letterhead .brand { position: absolute; top: 34px; left: 0; right: 0; }
  .letterhead .brand-mark { width: 70px; height: 70px; margin-bottom: 18px; }
  .letterhead .brand-name { font-size: 24px; }
  .letterhead .brand-sub { font-size: 14px; }
  .letterhead .brand-tag { font-size: 9px; margin-top: 4px; }
  .letterhead .faint-disc { position: absolute; left: 150px; top: 280px; width: 230px; height: 230px; border-radius: 50%; background: var(--purple-soft); opacity: .2; }
  .letterhead .wave { position: absolute; left: 0; bottom: 0; width: 100%; height: 130px; }
  .letterhead .footer-web { position: absolute; left: 16px; bottom: 14px; color: #fff; font-size: 8px; }
  .letterhead .footer-address { position: absolute; right: 16px; bottom: 12px; color: #fff; font-size: 7.5px; line-height: 1.5; text-align: right; }

  /* Business card front */
  .card-front { left: 643px; top: 168px; width: 216px; height: 101px; }
  .card-front .top { position: absolute; inset: 0 0 auto 0; height: 56px; background: var(--card-black); }
  .card-front .brand { padding-top: 6px; }
  .card-front .brand-mark { width: 16px; height: 16px; margin-bottom: 3px; }
  .card-front .brand-name { font-size: 10px; color: var(--green); }
  .card-front .brand-sub { font-size: 7px; color: #c9a3dd; }
  .card-front .wave { position: absolute; left: 0; top: 48px; width: 100%; height: 53px; }
  .card-front .person { position: absolute; left: 10px; top: 62px; font-size: 6.5px; color: var(--ink); line-height: 1.4; }
  .card-front .person strong { color: var(--purple); font-size: 7px; }

  /* Business card back */
  .card-back { left: 871px; top: 163px; width: 214px; height: 106px; background: linear-gradient(160deg, var(--lime), var(--green) 70%, var(--green-deep)); }
  .card-back .heading { position: absolute; top: 8px; left: 0; right: 0; text-align: center; font-size: 6.5px; font-weight: 700; color: var(--purple); }
  .card-back .badge-tall { position: absolute; left: 95px; top: 22px; width: 24px; height: 36px; background: #fff; }
  .card-back .badges { position: absolute; left: 10px; right: 10px; bottom: 12px; display: flex; justify-content: space-between; align-items: flex-end; }
  .card-back .badge { background: #fff; border-radius: 2px; height: 14px; }

  /* Envelope */
  .envelope { left: 571px; top: 319px; width: 511px; height: 363px; }
  .envelope .flap { position: absolute; left: 0; top: 0; width: 100%; height: 60px; }
  .envelope .flap-disc { position: absolute; left: 240px; top: 14px; width: 30px; height: 30px; border-radius: 50%; background: #fff; opacity: .25; }
  .envelope .brand { position: absolute; left: 0; right: 0; top: 76px; }
  .envelope .brand-mark { width: 62px; height: 62px; margin-bottom: 12px; }
  .envelope .brand-name { font-size: 22px; }
  .envelope .brand-sub { font-size: 13px; }
  .envelope .brand-tag { font-size: 8.5px; margin-top: 3px; }
  .envelope .wave { position: absolute; left: 0; bottom: 0; width: 100%; height: 140px; }
  .envelope .return-address { position: absolute; right: 16px; bottom: 14px; color: #fff; font-size: 7.5px; }
</style>
</head>
<body>

<section class="sheet letterhead">
  <div class="brand">
    <span class="brand-mark"></span>
    <div class="brand-name">CALVANE CHIROPRACTIC</div>
    <div class="brand-sub">MOTION AND VITALITY</div>
    <div class="brand-tag">MOVE, RESTORE &amp; STAY LIMBER...<br>IN YOUR STEP, IN YOUR DAY!</div>
  </div>
  <div class="faint-disc"></div>
  <svg class="wave" viewBox="0 0 521 130" preserveAspectRatio="none">
    <path d="M0 80 C160 120 330 10 521 50 L521 130 L0 130 Z" fill="var(--purple)"/>
    <path d="M0 92 C160 132 330 22 521 62 L521 130 L0 130 Z" fill="var(--green)"/>
  </svg>
  <div class="footer-web">www.GoDrMarla.net</div>
  <div class="footer-address">
    417 E Quarry Ln, Suite 83<br>
    PO Box 6289, Harrowby, PA 47310-2894<br>
    Phone 215-555-0148<br>
    Fax 215-555-0149<br>
    Dr.Marla@GoDrMarla.net
  </div>
</section>

<section class="sheet card-front">
  <div class="top">
    <div class="brand">
      <span class="brand-mark"></span>
      <div class="brand-name">CALVANE CHIROPRACTIC</div>
      <div class="brand-sub">MOTION AND VITALITY</div>
    </div>
  </div>
  <svg class="wave" viewBox="0 0 216 53" preserveAspectRatio="none">
    <path d="M0 8 C70 18 150 0 216 10 L216 0 L0 0 Z" fill="var(--card-black)"/>
    <path d="M0 40 C70 30 150 48 216 30 L216 53 L0 53 Z" fill="var(--purple)"/>
    <path d="M0 45 C70 36 150 53 216 36 L216 53 L0 53 Z" fill="var(--green)"/>
  </svg>
  <div class="person"><strong>Marla Teversham, D.C.</strong><br>Diplomate CSCAC&reg;</div>
</section>

<section class="sheet card-back">
  <div class="heading">Certified Practitioner in the Following:</div>
  <div class="badge-tall"></div>
  <div class="badges">
    <div class="badge" style="width:30px"></div>
    <div class="badge" style="width:26px"></div>
    <div class="badge" style="width:34px"></div>
    <div class="badge" style="width:24px"></div>
    <div class="badge" style="width:32px"></div>
  </div>
</section>

<section class="sheet envelope">
  <svg class="flap" viewBox="0 0 511 60" preserveAspectRatio="none">
    <defs>
      <linearGradient id="flapGrad" x1="0" y1="0" x2="0" y2="1">
        <stop offset="0" stop-color="var(--lime)"/>
        <stop offset="1" stop-color="var(--green)"/>
      </linearGradient>
    </defs>
    <path d="M0 0 H511 V42 C360 60 150 60 0 42 Z" fill="url(#flapGrad)"/>
  </svg>
  <div class="flap-disc"></div>
  <div class="brand">
    <span class="brand-mark"></span>
    <div class="brand-name">CALVANE CHIROPRACTIC</div>
    <div class="brand-sub">MOTION AND VITALITY</div>
    <div class="brand-tag">MOVE, RESTORE &amp; STAY LIMBER...<br>IN YOUR STEP, IN YOUR DAY!</div>
  </div>
  <svg class="wave" viewBox="0 0 511 140" preserveAspectRatio="none">
    <path d="M0 55 C140 100 330 20 511 45 L511 140 L0 140 Z" fill="var(--purple)"/>
    <path d="M0 66 C140 111 330 31 511 56 L511 140 L0 140 Z" fill="var(--green)"/>
  </svg>
  <div class="return-address">417 E Quarry Ln, Suite 83, Harrowby, PA 47310-2894</div>
</section>

</body>
</html>
```